Website Design Project for Beauty & Wellness Professionals

As background information, I have a website that is focused on Beauty & Wellness Professionals:
- Job Search (www.trilhavelora.com)
- Business Classifieds (negocios.trilhavelora.com)
- Freelancer Classifieds (freelancer.trilhavelora.com)
- Course Reviews (cursos.trilhavelora.com)

All those websites use standard templates.

I need a DESIGN for the HOME PAGE (no coding) of the Website Platform that consolidates the four platforms under the same design.

Website designs that we like:
- quovenda.com
- mirtelpeek.com

Target Market(s)

Brazilian Professionals from Beauty & Wellness sector

Industry/Entity Type

Business

Requirements
Must have
• Website designs that we like:
- quovenda.com
- mirtelpeek.com

```html
<!DOCTYPE html>
<html lang="pt">
<head>
<meta charset="utf-8">
<title>Trilha Velora</title>
<link href="https://fonts.googleapis.com/css2?family=Open+Sans:wght@400;600;700&display=swap" rel="stylesheet">
<style>
:root{
  --teal:#3a9dc0;
  --teal-dark:#1f7ea3;
  --teal-deep:#2b86a8;
  --green:#7cbd6c;
  --green-text:#4c9a3a;
  --ink:#333;
  --muted:#888;
  --line:#e3e3e3;
  --btn-dark:#555;
}
*{margin:0;padding:0;box-sizing:border-box}
html,body{width:718px;height:1200px;overflow:hidden;background:#fff;font-family:'Open Sans',Arial,sans-serif;color:var(--ink)}
.page{position:relative;width:718px;height:1200px}
.abs{position:absolute}
.brand{left:108px;top:8px;display:flex;flex-direction:column;align-items:flex-start}
.brand-mark{width:30px;height:30px;border-radius:50%;background:var(--teal);margin-left:26px}
.brand-name{margin-top:8px;font-size:19px;color:var(--teal);font-weight:400}
.top-btn{top:32px;height:17px;background:var(--teal);color:#fff;font-size:7px;display:flex;align-items:center;justify-content:center;border-radius:2px}
.nav{left:0;top:76px;width:718px;height:23px;background:var(--teal);display:flex;padding-left:108px}
.nav a{color:#fff;font-size:6px;font-weight:700;text-decoration:none;display:flex;align-items:center;height:23px;padding:0 17px}
.nav a.active{background:var(--teal-deep)}
.hero{left:0;top:99px;width:718px;height:253px;background:linear-gradient(90deg,#f2ece6 0%,#f6efe8 35%,#eef2f4 65%,#f5f7f8 100%)}
.hero-photo{left:70px;top:99px;width:300px;height:253px;background:radial-gradient(ellipse at 50% 45%,#f1d4b6 0%,#ead2bb 45%,rgba(240,234,228,0) 75%)}
.hero-title{left:432px;top:164px;font-size:20px;font-weight:700;color:var(--teal-dark)}
.hero-sub{left:434px;top:193px;font-size:12px;color:var(--green-text)}
.search{left:430px;top:219px;width:180px;height:17px;border:1px solid #d7dde0;background:#fff;display:flex}
.search span{flex:1;font-size:6.5px;color:var(--teal-dark);padding-left:8px;display:flex;align-items:center}
.search b{width:46px;background:var(--teal);color:#fff;font-size:6px;font-weight:400;display:flex;align-items:center;justify-content:center}
.hero-help{left:431px;top:244px;width:190px;font-size:6.5px;line-height:10px;color:#333}
.arrow{top:270px;width:15px;height:15px;background:var(--teal);display:flex;align-items:center;justify-content:center}
.sec-title{font-size:7.5px;font-weight:700;color:var(--teal-dark);padding-bottom:6px;border-bottom:3px solid var(--teal)}
.job{width:106px}
.job .ph{height:51px}
.job .cap{font-size:5.3px;color:var(--teal);line-height:9px;margin-top:6px}
.job .date{font-size:5px;font-style:italic;color:var(--muted);margin-top:7px;padding-bottom:4px;border-bottom:1px solid var(--line)}
.banner{left:108px;top:591px;width:344px;height:43px;background:linear-gradient(90deg,#8a2a82,#c4379a 50%,#6a3d8e)}
.pager{left:302px;top:944px;display:flex;gap:4px}
.pager span{width:11px;height:10px;border:1px solid #c66;font-size:5.5px;color:#c33;display:flex;align-items:center;justify-content:center}
.course{width:166px}
.course .ph{height:74px;margin-top:14px}
.course h4{font-size:6px;color:var(--green-text);margin-top:10px}
.course p{font-size:5.3px;line-height:9px;color:#555;margin-top:4px}
.course .row{display:flex;justify-content:space-between;align-items:center;margin-top:7px}
.course .cta{background:var(--btn-dark);color:#fff;font-size:5.5px;padding:5px 9px;border-radius:2px}
.course .brandlet{font-size:8px;font-weight:700;color:#555;display:flex;align-items:center;gap:2px}
.course .brandlet i{width:9px;height:9px;background:#e8702a;display:block}
.signup{left:470px;top:373px;width:140px;height:89px;background:var(--green);padding:9px 10px;color:#fff;border-radius:2px}
.signup h3{font-size:7px;font-weight:600}
.signup p{font-size:5px;line-height:8px;margin-top:6px}
.signup .in{background:#fff;height:11px;border-radius:6px;margin-top:6px;color:#aaa;font-size:5px;padding-left:8px;display:flex;align-items:center}
.signup .go{margin:7px 0 0 auto;width:44px;height:10px;background:var(--btn-dark);font-size:4.5px;display:flex;align-items:center;justify-content:center;border-radius:2px}
.ad{left:474px;top:467px;width:128px;height:127px;background:linear-gradient(135deg,#f3ead8,#e9d3b4);border:2px solid #9b2c24}
.cats{left:470px;top:612px;width:140px}
.cats ul{list-style:none;margin-top:6px}
.cats li{font-size:4.8px;color:#444;height:15px;display:flex;align-items:center;padding-left:4px;border-bottom:1px solid var(--line);width:132px}
.tabs{left:474px;top:893px;display:flex}
.tabs span{height:16px;width:48px;font-size:5px;color:#fff;display:flex;align-items:center;justify-content:center}
.tabbox{left:470px;top:909px;width:140px;height:69px;border:1px solid var(--line);padding:3px 8px}
.tabbox div{font-size:4.8px;color:#444;height:15.5px;display:flex;align-items:center;border-bottom:1px solid var(--line)}
.social{left:472px;width:136px;height:24px;border-radius:12px;background:linear-gradient(#fafafa,#dcdcdc);box-shadow:0 1px 2px rgba(0,0,0,.3);display:flex;align-items:center}
.social i{width:24px;height:24px;border-radius:50%;display:block;flex:none}
.social span{flex:1;text-align:center;font-size:6.5px;font-weight:700;color:#555}
.footer{left:0;top:1156px;width:718px;height:44px;background:var(--teal);color:#fff;text-align:center}
.footer nav{font-size:5px;margin-top:12px;display:flex;justify-content:center;gap:8px}
.footer p{font-size:5px;margin-top:7px}
</style>
</head>
<body>
<div class="page">
  <div class="abs brand"><span class="brand-mark"></span><span class="brand-name">Trilha Velora</span></div>
  <div class="abs top-btn" style="left:430px;width:105px">Anuncie vags Emprego</div>
  <div class="abs top-btn" style="left:522px;width:87px">Entrar/Cadastre-se</div>

  <nav class="abs nav">
    <a class="active" href="#">HOME</a><a href="#">BLOG</a><a href="#">PARA PROFISSIONAIS</a><a href="#">PARA EMPRESAS</a><a href="#">EVENTOS&amp;PARCEIROS</a><a href="#">SOBRE NOS</a><a href="#">FALE CONOSCO</a>
  </nav>

  <div class="abs hero"></div>
  <div class="abs hero-photo" role="img" aria-label="Foto de mulher loira aplicando batom diante de um espelho"></div>
  <div class="abs hero-title">Trilha Velora</div>
  <div class="abs hero-sub">Vagas de Emprego em Destaque</div>
  <div class="abs search"><span>Escreva aqui Profissao e Local</span><b>SEARCH</b></div>
  <div class="abs hero-help">Busque Profissão e Local desejados! Ex: Manicure São Paulo, Cabeleireira Rio de Janeiro</div>
  <div class="abs arrow" style="left:574px"><svg width="5" height="7"><path d="M4 0L0 3.5 4 7" fill="none" stroke="#fff"/></svg></div>
  <div class="abs arrow" style="left:594px"><svg width="5" height="7"><path d="M1 0L5 3.5 1 7" fill="none" stroke="#fff"/></svg></div>

  <div class="abs sec-title" style="left:108px;top:364px;width:344px">VAGAS DE EMPREGO EM DESTAQUE</div>

  <div class="abs job" style="left:108px;top:391px"><div class="ph" role="img" aria-label="Foto de mulher de cabelos castanhos" style="background:linear-gradient(135deg,#6b4a3a,#c89a7a)"></div><div class="cap">AUX. CABELEIREIRO (ESCOVISTA) – SANTO ANDRÉ (SP)</div><div class="date">18 jul 2013</div></div>
  <div class="abs job" style="left:227px;top:391px"><div class="ph" role="img" aria-label="Foto de maquiagem sendo aplicada" style="background:linear-gradient(135deg,#2a2230,#7a4e8c)"></div><div class="cap">AUX. CABELEIREIRO (ESCOVISTA) – SANTO ANDRÉ (SP)</div><div class="date">18 jul 2013</div></div>
  <div class="abs job" style="left:346px;top:391px"><div class="ph" role="img" aria-label="Foto de mulher com pincéis de maquiagem" style="background:linear-gradient(135deg,#f0dcc6,#b68a66)"></div><div class="cap">AUX. CABELEIREIRO (ESCOVISTA) – SANTO ANDRÉ (SP)</div><div class="date">18 jul 2013</div></div>

  <div class="abs job" style="left:108px;top:494px"><div class="ph" role="img" aria-label="Foto de homem sorrindo" style="background:linear-gradient(135deg,#3d6f9c,#c79d7c)"></div><div class="cap">AUX. CABELEIREIRO (ESCOVISTA) – SANTO ANDRÉ (SP)</div><div class="date">18 jul 2013</div></div>
  <div class="abs job" style="left:227px;top:494px"><div class="ph" role="img" aria-label="Foto de mulher sorridente deitada" style="background:linear-gradient(135deg,#f4ebe2,#dcb88f)"></div><div class="cap">AUX. CABELEIREIRO (ESCOVISTA) – SANTO ANDRÉ (SP)</div><div class="date">18 jul 2013</div></div>
  <div class="abs job" style="left:346px;top:494px"><div class="ph" role="img" aria-label="Foto de maquiagem colorida nos olhos" style="background:linear-gradient(135deg,#3b3b3b,#b7b43a 55%,#e0c0a8)"></div><div class="cap">AUX. CABELEIREIRO (ESCOVISTA) – SANTO ANDRÉ (SP)</div><div class="date">18 jul 2013</div></div>

  <div class="abs banner" role="img" aria-label="Banner publicitário de marketing para negócios em casa"></div>

  <div class="abs job" style="left:108px;top:646px"><div class="ph" role="img" aria-label="Foto de mulher sorrindo" style="background:linear-gradient(135deg,#e6eef0,#c49a7e)"></div><div class="cap">AUX. CABELEIREIRO (ESCOVISTA) – SANTO ANDRÉ (SP)</div><div class="date">18 jul 2013</div></div>
  <div class="abs job" style="left:227px;top:646px"><div class="ph" role="img" aria-label="Foto de rosto com maquiagem" style="background:linear-gradient(135deg,#c98d6e,#f2d2b8)"></div><div class="cap">AUX. CABELEIREIRO (ESCOVISTA) – SANTO ANDRÉ (SP)</div><div class="date">18 jul 2013</div></div>
  <div class="abs job" style="left:346px;top:646px"><div class="ph" role="img" aria-label="Foto de casal sorrindo" style="background:linear-gradient(135deg,#efe9e2,#a7683f)"></div><div class="cap">AUX. CABELEIREIRO (ESCOVISTA) – SANTO ANDRÉ (SP)</div><div class="date">18 jul 2013</div></div>

  <div class="abs job" style="left:108px;top:748px"><div class="ph" role="img" aria-label="Foto de paleta de sombras e maquiagem" style="background:linear-gradient(135deg,#b07a58,#e8d4c2)"></div><div class="cap">AUX. CABELEIREIRO (ESCOVISTA) – SANTO ANDRÉ (SP)</div><div class="date">18 jul 2013</div></div>
  <div class="abs job" style="left:227px;top:748px"><div class="ph" role="img" aria-label="Foto de mulher de cabelo curto" style="background:linear-gradient(135deg,#e8ecee,#8c6a55)"></div><div class="cap">AUX. CABELEIREIRO (ESCOVISTA) – SANTO ANDRÉ (SP)</div><div class="date">18 jul 2013</div></div>
  <div class="abs job" style="left:346px;top:748px"><div class="ph" role="img" aria-label="Foto de homem de braços abertos sob o céu" style="background:linear-gradient(180deg,#2c6aa8,#8cb8df)"></div><div class="cap">AUX. CABELEIREIRO (ESCOVISTA) – SANTO ANDRÉ (SP)</div><div class="date">18 jul 2013</div></div>

  <div class="abs job" style="left:108px;top:845px"><div class="ph" role="img" aria-label="Foto de amigas fazendo compras" style="background:linear-gradient(135deg,#a07a62,#e6d2c0)"></div><div class="cap">AUX. CABELEIREIRO (ESCOVISTA) – SANTO ANDRÉ (SP)</div><div class="date">18 jul 2013</div></div>
  <div class="abs job" style="left:227px;top:845px"><div class="ph" role="img" aria-label="Foto de mulher com flores rosas" style="background:linear-gradient(135deg,#c43a8a,#3a2a3a)"></div><div class="cap">AUX. CABELEIREIRO (ESCOVISTA) – SANTO ANDRÉ (SP)</div><div class="date">18 jul 2013</div></div>
  <div class="abs job" style="left:346px;top:845px"><div class="ph" role="img" aria-label="Foto de lábios vermelhos e unhas pintadas" style="background:linear-gradient(135deg,#f2e2d6,#b8282e)"></div><div class="cap">AUX. CABELEIREIRO (ESCOVISTA) – SANTO ANDRÉ (SP)</div><div class="date">18 jul 2013</div></div>

  <div class="abs pager"><span>‹</span><span>1</span><span>2</span><span>3</span><span>4</span><span>5</span><span>6</span><span>7</span><span>8</span><span>›</span></div>

  <div class="abs course" style="left:108px;top:968px"><div class="sec-title">CURSOS ONLINE APRENVO</div><div class="ph" role="img" aria-label="Foto de mulher com maquiagem marcante" style="background:linear-gradient(135deg,#3a2a36,#a06a66)"></div><h4>CURSOS ONLINE APRENVO</h4><p>Lorem Ipsum is simply dummy text of the printing and typesetting industry. Lorem Ipsum has been the industry's standard dummy text ever since the 1500s</p><div class="row"><span class="cta">EXPERIMENT GRATIS</span><span class="brandlet">aprenvo<i></i></span></div></div>
  <div class="abs course" style="left:286px;top:968px"><div class="sec-title">CURSOS ONLINE APRENVO</div><div class="ph" role="img" aria-label="Foto de mulher sorrindo apoiada nas mãos" style="background:linear-gradient(135deg,#8a5a3e,#f0e0d2)"></div><h4>CURSOS ONLINE APRENVO</h4><p>Lorem Ipsum is simply dummy text of the printing and typesetting industry. Lorem Ipsum has been the industry's standard dummy text ever since the 1500s</p><div class="row"><span class="cta">EXPERIMENT GRATIS</span><span class="brandlet">aprenvo<i></i></span></div></div>

  <div class="abs signup"><h3>ASSINAR POR EMAIL</h3><p>Digite seu endereço de email para assinar e receber notificações de novas vagas por email.</p><div class="in">Assinar por Email</div><div class="go">SUBSCRIBE</div></div>
  <div class="abs ad" role="img" aria-label="Anúncio ilustrado de curso de relacionamentos"></div>

  <div class="abs cats"><div class="sec-title">VAGAS DE EMPREGO</div><ul>
    <li>AUXILIAR CABELEIREIRO</li><li>AUXILIAR LIMPEZA</li><li>CABELEIREIRO</li><li>DEPILADORA</li><li>DESIGNER SOBRANCELHA</li><li>DESTAQUE</li><li>ENFERMEIRA</li><li>ESTETICISTA</li><li>FISIOTERAPEUTA</li><li>GERÊNCIA/COORDENAÇÃO</li><li>MANICURE E PEDICURE</li><li>MAQUIADOR</li><li>MASSOTERAPEUTA</li><li>OUTROS</li><li>PODÓLOGO</li><li>RECEPÇÃO/ATENDIMENTO</li><li>VENDAS COSMÉTICOS</li>
  </ul></div>

  <div class="abs tabs"><span style="background:var(--teal)">BUSCAR POR</span><span style="background:var(--green)">TAGS</span></div>
  <div class="abs tabbox"><div>TIPO DE VAGA DE EMPREGO</div><div>SALÁRIO DA VAGA</div><div>CATEGORIA DA VAGA</div><div>DATA DE PUBLICAÇÃO</div></div>

  <div class="abs social" style="top:993px"><i style="background:#3b5a9a"></i><span>Connect to Rostra</span></div>
  <div class="abs social" style="top:1024px"><i style="background:#3aa6d8"></i><span>Follow on Chirpwell</span></div>
  <div class="abs social" style="top:1056px"><i style="background:#2e6f95"></i><span>Connect on Searlo +</span></div>
  <div class="abs social" style="top:1087px"><i style="background:#ef7a1e"></i><span>Subscribe to RSS</span></div>

  <footer class="abs footer">
    <nav><span>Home</span><span>|</span><span>Blog</span><span>|</span><span>Para Profissionais</span><span>|</span><span>Para Empresas</span><span>|</span><span>Eventos&amp;Parceiros</span><span>|</span><span>Sobre NÓS</span><span>|</span><span>Fale Conosco</span></nav>
    <p>Copyright @ 2013 Trilha Velora. All rights reserved.</p>
  </footer>
</div>
</body>
</html>
```